Business Card Design Project

We need a Business Card for an Mechanical Engineering firm in Singapore. The design should be Modern & Technical looking, yet eye catching.

Our company deals in Cutting Tools & Machine Accessories for the Manufacturing Industries such as Oil & Gas, Aero Space, etc... For more information on our Company, you can either email me or view our website www.valtrion.com.sg.

We are trying to revamp our image to give our consumers a fresh new perspective to our company, so we welcome all ideas.

Industry/Entity Type

Business

Requirements
Must have
• Must incorporate New Company Logo into the card as shown in Uploaded file.

```html
<!DOCTYPE html>
<html lang="en">
<head>
<meta charset="utf-8">
<title>Valtrion Tools – Business Card</title>
<link href="https://fonts.googleapis.com/css2?family=Mulish:wght@400;700&display=swap" rel="stylesheet">
<style>
  :root {
    --maroon: #8b0f3e;
    --ink: #1f1f1f;
    --card: #ffffff;
    --backdrop: #b9c1ab;
  }
  * { box-sizing: border-box; margin: 0; padding: 0; }
  html, body {
    width: 1200px;
    height: 900px;
    overflow: hidden;
  }
  body {
    background: var(--backdrop);
    font-family: "Mulish", "Century Gothic", sans-serif;
    color: var(--ink);
    position: relative;
  }
  .card {
    position: absolute;
    top: 305px;
    width: 500px;
    height: 290px;
    background: var(--card);
    border-radius: 28px;
    box-shadow: 0 4px 14px rgba(0, 0, 0, 0.25);
  }
  .card--front { left: 70px; }
  .card--back { left: 630px; }

  .holder { position: absolute; left: 30px; top: 26px; }
  .holder__name {
    color: var(--maroon);
    font-weight: 700;
    font-size: 19px;
    line-height: 22px;
  }
  .holder__role { font-size: 16px; line-height: 20px; }

  .contact {
    position: absolute;
    right: 30px;
    top: 24px;
    list-style: none;
    text-align: right;
    font-size: 16px;
    line-height: 20px;
  }
  .contact__label { color: var(--maroon); }

  .web-rule {
    position: absolute;
    left: 30px;
    right: 30px;
    top: 132px;
    display: flex;
    align-items: center;
    gap: 6px;
  }
  .web-rule__line {
    flex: 1;
    border-top: 1px dashed var(--maroon);
  }
  .web-rule__url { color: var(--maroon); font-size: 17px; }

  .address {
    position: absolute;
    left: 30px;
    top: 178px;
    font-style: normal;
    font-size: 16px;
    line-height: 20px;
  }
  .address__company { color: var(--maroon); }

  .brand {
    position: absolute;
    display: flex;
    align-items: center;
    color: var(--maroon);
    font-weight: 700;
    white-space: nowrap;
  }
  .brand--small {
    right: 30px;
    bottom: 30px;
    font-size: 15px;
    gap: 6px;
  }
  .brand--large {
    left: 50%;
    top: 50%;
    transform: translate(-50%, -50%);
    font-size: 32px;
    gap: 12px;
  }
</style>
</head>
<body>
  <section class="card card--front" aria-label="Business card front">
    <div class="holder">
      <p class="holder__name">Marcus Lim</p>
      <p class="holder__role">Manager</p>
    </div>
    <ul class="contact">
      <li><span class="contact__label">tel:</span> 656 310 2947</li>
      <li><span class="contact__label">mob:</span> 987 654 3210</li>
      <li><span class="contact__label">fax:</span> 656 310 2948</li>
      <li>info@valtrion.com.sg</li>
    </ul>
    <div class="web-rule">
      <span class="web-rule__line"></span>
      <span class="web-rule__url">www.valtrion.com.sg</span>
    </div>
    <address class="address">
      <span class="address__company">Valtrion Tools Pte Ltd.</span><br>
      27 Kallang Way #05-12<br>
      Kallang Industrial Park<br>
      Singapore 349215
    </address>
    <div class="brand brand--small">
      <svg width="16" height="16" viewBox="0 0 16 16" aria-hidden="true"><circle cx="8" cy="8" r="7" fill="var(--maroon)"/></svg>
      <span>VALTRION TOOLS</span>
    </div>
  </section>

  <section class="card card--back" aria-label="Business card back">
    <div class="brand brand--large">
      <svg width="34" height="34" viewBox="0 0 34 34" aria-hidden="true"><circle cx="17" cy="17" r="16" fill="var(--maroon)"/></svg>
      <span>VALTRION TOOLS</span>
    </div>
  </section>
</body>
</html>
```